2in1 Bartender & Sommelier needs a business card

I need a business card. I worked as a bartender in many places but I just finished a sommelier school and I would like a new business card. I like minimal design, natural materials and something what makes the people think :) I try to be creative in cocktail making, like little mixology, little twist on recipes... I like to travel and discover new places, cultures and of course interesting drinks and improve continously...live a little bit crazy life. And I like what I do...

Target Market(s)

restaurant/winebar managers, winemakers, other sommeliers and bartenders, people who work in food and beverage sector

Industry/Entity Type

Hospitality

Contact Information for Business Card

Réka Fodor
Bartender & Sommelier
Phone: (FR) +33 6 4720 3917
(HU) +36 70 518 6092

Font styles to use
Script

Requirements
Must have
• Some sign, I am a bartender and sommelier as well.
Nice to have
• black and white maybe with 1 or 2 extra color
Should not have
• very colourful, to many things on the card

```html
<!DOCTYPE html>
<html lang="en">
<head>
<meta charset="UTF-8">
<title>Réka Fodor — Business Card</title>
<link href="https://fonts.googleapis.com/css2?family=Montserrat:wght@400;500;800&display=swap" rel="stylesheet">
<style>
  :root {
    --backdrop: #3b2b23;
    --ink: #050808;
    --paper: #ffffff;
    --accent: #f2b71f;
    --muted-glass: #c9c9c9;
  }
  * { box-sizing: border-box; margin: 0; padding: 0; }
  html, body { width: 1200px; height: 1000px; overflow: hidden; }
  body {
    position: relative;
    background: var(--backdrop);
    font-family: "Montserrat", sans-serif;
  }
  .card {
    position: absolute;
    width: 525px;
    height: 299px;
    overflow: hidden;
  }
  .card--front { left: 145px; top: 145px; background: var(--paper); }
  .card--back { left: 488px; top: 498px; background: var(--ink); }

  .front__lower {
    position: absolute; left: 0; right: 0; top: 162px; bottom: 0;
    background: var(--ink);
  }
  .front__glassware {
    position: absolute; left: 50px; top: 48px; width: 190px; height: 56px;
    background: linear-gradient(90deg, #9a9a9a, #1e1e1e 40%, #7d7d7d 60%, #1b1b1b 85%, #b0b0b0);
    opacity: 0.85;
  }
  .front__name-panel {
    position: absolute; left: 47px; top: 105px; width: 196px; height: 122px;
    background: var(--paper);
    border: 6px solid var(--ink);
    display: flex; flex-direction: column; justify-content: center; align-items: center;
  }
  .wordmark {
    font-weight: 800;
    line-height: 1.02;
    text-align: center;
    letter-spacing: 0.5px;
  }
  .front__name-panel .wordmark { color: var(--ink); font-size: 36px; }
  .front__accent-bar {
    position: absolute; left: 55px; top: 231px; width: 182px; height: 15px;
    background: var(--accent);
  }
  .front__identity { position: absolute; left: 278px; top: 114px; }
  .identity__name {
    font-weight: 800; font-size: 20px; color: var(--ink); letter-spacing: 0.3px;
  }
  .identity__role {
    font-weight: 400; font-size: 15px; color: #222; margin-top: 2px;
  }
  .front__contacts {
    position: absolute; left: 280px; top: 186px; list-style: none;
  }
  .contact {
    display: flex; align-items: center; gap: 10px;
    color: var(--paper); font-size: 13.5px; font-weight: 400;
    height: 21.5px;
  }
  .contact svg { width: 16px; height: 16px; flex: none; }

  .back__logo {
    position: absolute; left: 0; right: 0; top: 0; bottom: 0;
    display: flex; justify-content: center; align-items: center;
  }
  .back__logo .wordmark { color: var(--paper); font-size: 38px; }
</style>
</head>
<body>

<section class="card card--front" aria-label="Business card front">
  <div class="front__lower"></div>
  <div class="front__glassware" role="img" aria-label="Row of cocktail glasses and wine bottles"></div>
  <div class="front__name-panel">
    <div class="wordmark">RÉKA<br>FODOR</div>
  </div>
  <div class="front__accent-bar"></div>

  <div class="front__identity">
    <div class="identity__name">RÉKA FODOR</div>
    <div class="identity__role">Bartender &amp; Sommelier</div>
  </div>

  <ul class="front__contacts">
    <li class="contact">
      <svg viewBox="0 0 16 16" aria-hidden="true"><circle cx="8" cy="8" r="8" fill="#fff"/><path d="M4.5 6.2c0-1 1.6-1.7 3.5-1.7s3.5.7 3.5 1.7v.6H10v-.7H6v.7H4.5z M5.2 7.5h5.6l.7 3.6H4.5z" fill="#050808"/></svg>
      <span>(FR) +33 6 4720 3917</span>
    </li>
    <li class="contact">
      <svg viewBox="0 0 16 16" aria-hidden="true"><circle cx="8" cy="8" r="8" fill="#fff"/><path d="M4.5 6.2c0-1 1.6-1.7 3.5-1.7s3.5.7 3.5 1.7v.6H10v-.7H6v.7H4.5z M5.2 7.5h5.6l.7 3.6H4.5z" fill="#050808"/></svg>
      <span>(HU) +36 70 518 6092</span>
    </li>
    <li class="contact">
      <svg viewBox="0 0 16 16" aria-hidden="true"><circle cx="8" cy="8" r="8" fill="#fff"/><rect x="4" y="5.2" width="8" height="5.6" fill="#050808"/><path d="M4 5.2l4 3 4-3" stroke="#fff" stroke-width="0.8" fill="none"/></svg>
      <span>fodorreka84@mailbox.com</span>
    </li>
  </ul>
</section>

<section class="card card--back" aria-label="Business card back">
  <div class="back__logo">
    <div class="wordmark">RÉKA<br>FODOR</div>
  </div>
</section>

</body>
</html>
```